Business card design for sustainable building and development company

Need a business card design for a new sustainable building and real estate development company in the San Francisco Bay area. Name of company is "HNX Consultants, LLC" and we provide "Sustainable building, energy and development services" for residential and non residential projects. We'd like the following colors used but not all area required: green, gray, blue. Design should communicate innovation, professionalism and sustainability. Our current website is www.hnx-consultants.com. Another possible design idea is to have the following listed on the back of the card:
Certified: TORV AP, Ecomark Rater, KWIL Rater, NovaTerra Inspector, DQX RT Building Analyst. Its not a must but could be text that could be used for back of card. Overall, we are open to a simple, clean design and or one with more text than usual for a card.

Industry/Entity Type

Real Estate

Contact Information for Business Card

Name on card: Derek M. Halvorsen
Title for Name: Principal + Founder
Phone: 555.555.0184
Email: dhalvorsen@hnx-consultants.com
Website: www.hnx-consultants.com

Also, please add the following for address:
Harborview, Calistra

Requirements
Nice to have
• If you can integrate the outline of a skyline on the backside of the card and if it looks good, I would like to see the design
Should not have
• a barcode;

```html
<!DOCTYPE html>
<html lang="en">
<head>
<meta charset="utf-8">
<title>HNX Consultants – Business Card</title>
<link rel="stylesheet" href="https://fonts.googleapis.com/css2?family=Open+Sans:wght@400;600;700;800&display=swap">
<style>
  :root {
    --bg: #3b3937;
    --card-white: #ffffff;
    --card-fade: #e6e8e7;
    --green: #5cc13a;
    --green-light: #7ed957;
    --green-dark: #2f7d22;
    --green-deep: #1f4f17;
    --text-dark: #3a3a3a;
    --text-green: #3d9a2a;
  }
  * { box-sizing: border-box; margin: 0; padding: 0; }
  html, body { width: 1200px; height: 900px; overflow: hidden; }
  body {
    background: var(--bg);
    font-family: "Open Sans", sans-serif;
    position: relative;
  }
  .card {
    position: absolute;
    width: 540px;
    height: 309px;
    background: linear-gradient(180deg, var(--card-white) 0%, var(--card-fade) 100%);
    overflow: hidden;
    box-shadow: 0 14px 30px rgba(0,0,0,.45);
  }
  .card--front { left: 40px; top: 295px; }
  .card--back  { left: 620px; top: 295px; }

  /* Front */
  .front__panel {
    position: absolute; left: 0; top: 0; bottom: 34px; width: 205px;
    background: linear-gradient(180deg, var(--green-light) 0%, var(--green) 70%, var(--green-dark) 100%);
  }
  .front__panel-shadow {
    position: absolute; left: 0; bottom: 0; width: 205px; height: 34px;
    background: linear-gradient(180deg, #d9dcda 0%, #b9bdbb 100%);
  }
  .front__brand {
    position: absolute; left: 0; width: 205px; top: 76px;
    display: flex; flex-direction: column; align-items: center; gap: 10px;
  }
  .front__brand-circle {
    width: 96px; height: 96px; border-radius: 50%;
    background: var(--green-dark);
  }
  .front__brand-name {
    font-weight: 700; font-size: 15px; color: var(--card-white);
  }
  .front__stripe {
    position: absolute; left: 205px; right: 0; top: 258px; height: 8px;
    background: var(--green);
  }
  .front__info {
    position: absolute; left: 232px; top: 62px; right: 16px;
  }
  .person__name { font-size: 21px; font-weight: 700; color: var(--text-green); line-height: 1.1; }
  .person__title { font-size: 15px; font-weight: 700; color: var(--text-green); margin-bottom: 16px; }
  .contact { display: grid; grid-template-columns: 58px 12px 1fr; font-size: 11px; color: var(--text-dark); line-height: 1.45; }

  /* Back */
  .back__brand {
    position: absolute; left: 34px; top: 60px;
    display: flex; align-items: center; gap: 16px;
  }
  .back__brand-circle {
    width: 82px; height: 82px; border-radius: 50%; background: var(--green);
    flex-shrink: 0;
  }
  .back__brand-name { font-size: 38px; font-weight: 800; color: var(--text-green); line-height: 1; }
  .back__tagline { font-size: 10.5px; color: var(--text-dark); letter-spacing: .2px; margin-top: 6px; text-transform: uppercase; }
  .back__band-dark {
    position: absolute; left: 0; right: 0; top: 196px; height: 12px; background: var(--green-deep);
  }
  .back__band {
    position: absolute; left: 0; right: 0; top: 208px; bottom: 0;
    background: linear-gradient(180deg, var(--green) 0%, var(--green-light) 100%);
    display: flex; flex-direction: column; justify-content: center; align-items: flex-end;
    padding-right: 22px; text-align: right;
  }
  .certs__label { font-size: 11px; color: var(--green-deep); }
  .certs__list { font-size: 11px; color: var(--green-deep); }
</style>
</head>
<body>
  <section class="card card--front" aria-label="Business card front">
    <div class="front__panel"></div>
    <div class="front__panel-shadow"></div>
    <div class="front__brand">
      <div class="front__brand-circle"></div>
      <div class="front__brand-name">HNX Consultants</div>
    </div>
    <div class="front__stripe"></div>
    <div class="front__info">
      <h1 class="person__name">Derek M. Halvorsen</h1>
      <p class="person__title">Principal / Owner</p>
      <div class="contact">
        <span>Phone</span><span>:</span><span>555.555.0184</span>
        <span>Email</span><span>:</span><span>dhalvorsen@hnx-consultants.com</span>
        <span>Website</span><span>:</span><span>www.hnx-consultants.com</span>
        <span>Address</span><span>:</span><span>Harborview, Calistra</span>
      </div>
    </div>
  </section>

  <section class="card card--back" aria-label="Business card back">
    <div class="back__brand">
      <div class="back__brand-circle"></div>
      <div>
        <div class="back__brand-name">HNX Consultants</div>
        <div class="back__tagline">Sustainable Building Energy &amp; Development Services</div>
      </div>
    </div>
    <div class="back__band-dark"></div>
    <div class="back__band">
      <p class="certs__label">Certified:</p>
      <p class="certs__list">TORV AP, Ecomark Rater, KWIL Rater, NovaTerra Inspector, DQX RT Building Analyst</p>
    </div>
  </section>
</body>
</html>
```